New business card/stationary for a consulting company

I am looking for a clean and very professional looking business card for my consulting company as well as corresponding stationary. I am uploading our logo. I like simple and powerful for the feel. No graphics but I am open on everything else. Below is my contact information but would like the final to be in a version I can add my employees information into and print. Thank you.

Daniel Whitcombe
dan@ferncrestadvisory.com
2738 North 17th Avenue, Summit Floor, Oak Brook, Illinois 60126
www.ferncrestadvisory.com

Industry/Entity Type

Consulting

Contact Information for Business Card

Daniel Whitcombe
dan@ferncrestadvisory.com
www.ferncrestadvisory.com

Font styles to use
Serif
Sans Serif

Requirements
Must have
• Our logo and the business card details.
Nice to have
• our website www.ferncrestadvisory.com

```html
<!DOCTYPE html>
<html lang="en">
<head>
<meta charset="utf-8">
<title>Ferncrest Advisory – Business Card</title>
<link rel="stylesheet" href="https://fonts.googleapis.com/css2?family=Questrial&family=Gelasio:wght@400;700&display=swap">
<style>
  :root {
    --navy: #0a0f8a;
    --navy-deep: #030654;
    --navy-mid: #0b13a8;
    --paper: #ffffff;
    --ink: #111111;
    --stage: #e6e7ea;
  }
  * { box-sizing: border-box; margin: 0; padding: 0; }
  html, body { width: 1200px; height: 900px; overflow: hidden; }
  body {
    background: var(--stage);
    position: relative;
    font-family: "Gelasio", Georgia, serif;
  }
  .card {
    position: absolute;
    left: 340px;
    width: 520px;
    height: 297px;
    overflow: hidden;
    box-shadow: 0 6px 18px rgba(0,0,0,0.18);
  }

  /* Front */
  .card-front {
    top: 110px;
    background: radial-gradient(ellipse at 55% 60%, var(--navy-mid) 0%, var(--navy) 45%, var(--navy-deep) 100%);
    color: var(--paper);
  }
  .card-front .brand {
    position: absolute;
    left: 48px;
    top: 96px;
    display: flex;
    align-items: center;
    gap: 14px;
    white-space: nowrap;
  }
  .card-front .brand-mark {
    width: 28px; height: 28px;
    background: var(--paper);
  }
  .card-front .brand-name {
    font-family: "Questrial", Arial, sans-serif;
    font-size: 33px;
    line-height: 1;
    letter-spacing: 1.5px;
    color: var(--paper);
  }
  .card-front .rule {
    position: absolute;
    left: 0; top: 166px;
    width: 250px; height: 2px;
    background: var(--paper);
  }
  .card-front .web {
    position: absolute;
    left: 262px; top: 155px;
    font-size: 15px;
    letter-spacing: 0.3px;
    white-space: nowrap;
  }

  /* Back */
  .card-back {
    top: 493px;
    background: var(--paper);
    color: var(--ink);
  }
  .card-back .band {
    position: absolute;
    left: 0; top: 0;
    width: 160px; height: 100%;
    background: linear-gradient(90deg, var(--navy-deep), var(--navy));
  }
  .card-back .band-brand {
    position: absolute;
    left: 80px; top: 148px;
    transform: translate(-50%, -50%) rotate(-90deg);
    display: flex; align-items: center; gap: 12px;
    white-space: nowrap;
  }
  .card-back .band-brand .brand-mark {
    width: 18px; height: 18px; background: var(--paper);
  }
  .card-back .band-brand .brand-name {
    font-family: "Questrial", Arial, sans-serif;
    font-size: 19px;
    line-height: 1;
    letter-spacing: 1.5px;
    color: var(--paper);
  }
  .card-back .divider {
    position: absolute;
    left: 300px; top: 0;
    width: 2px; height: 98px;
    background: var(--navy);
  }
  .card-back .details {
    position: absolute;
    left: 196px; top: 122px;
  }
  .card-back .person {
    font-weight: 700;
    font-size: 20px;
    text-transform: uppercase;
    color: var(--navy);
    letter-spacing: 0.2px;
    margin-bottom: 12px;
  }
  .contact-list { list-style: none; }
  .contact-list li {
    display: flex; align-items: flex-start; gap: 10px;
    font-size: 14px; line-height: 19px;
    margin-bottom: 6px;
    white-space: nowrap;
  }
  .contact-icon {
    flex: none;
    width: 20px; height: 20px;
  }
</style>
</head>
<body>

  <section class="card card-front" aria-label="Business card front">
    <div class="brand">
      <span class="brand-mark"></span>
      <span class="brand-name">FERNCREST ADVISORY</span>
    </div>
    <div class="rule"></div>
    <p class="web">www.ferncrestadvisory.com</p>
  </section>

  <section class="card card-back" aria-label="Business card back">
    <div class="band">
      <div class="band-brand">
        <span class="brand-mark"></span>
        <span class="brand-name">FERNCREST ADVISORY</span>
      </div>
    </div>
    <div class="divider"></div>
    <div class="details">
      <h1 class="person">Daniel Whitcombe</h1>
      <ul class="contact-list">
        <li>
          <svg class="contact-icon" viewBox="0 0 20 20" aria-hidden="true">
            <rect x="1" y="1" width="18" height="18" fill="none" stroke="#0a0f8a" stroke-width="1.6"/>
            <rect x="5" y="6.5" width="10" height="7" fill="none" stroke="#0a0f8a" stroke-width="1.3"/>
            <path d="M5 6.5 L10 10.5 L15 6.5" fill="none" stroke="#0a0f8a" stroke-width="1.3"/>
          </svg>
          <span>dan@ferncrestadvisory.com</span>
        </li>
        <li>
          <svg class="contact-icon" viewBox="0 0 20 20" aria-hidden="true">
            <rect x="1" y="1" width="18" height="18" fill="none" stroke="#0a0f8a" stroke-width="1.6"/>
            <circle cx="10" cy="10" r="5" fill="none" stroke="#0a0f8a" stroke-width="1.3"/>
            <path d="M5 10 H15 M10 5 C7.5 8 7.5 12 10 15 M10 5 C12.5 8 12.5 12 10 15" fill="none" stroke="#0a0f8a" stroke-width="1"/>
          </svg>
          <span>www.ferncrestadvisory.com</span>
        </li>
        <li>
          <svg class="contact-icon" viewBox="0 0 20 20" aria-hidden="true">
            <rect x="1" y="1" width="18" height="18" fill="none" stroke="#0a0f8a" stroke-width="1.6"/>
            <path d="M10 15.5 C7 12 6 10.3 6 8.6 A4 4 0 0 1 14 8.6 C14 10.3 13 12 10 15.5 Z" fill="none" stroke="#0a0f8a" stroke-width="1.3"/>
            <circle cx="10" cy="8.6" r="1.5" fill="#0a0f8a"/>
          </svg>
          <span>2738 North 17th Avenue, Summit Floor,<br>Maple Ridge, Illinois 60599</span>
        </li>
      </ul>
    </div>
  </section>

</body>
</html>
```